Recrutering company needs a Roll-Up Design

We need a Roll-Up Design for our company, which is dedicated to personnel selection. We would like the roll-up to feature our logo and the silhouette of the buildings shown in one of the uploaded photos (the one called "BelorquiFestuOre7"). Additionally, we'd like to incorporate the words "Persones," "Talent," and "Èxit" with shadows using the English equivalents instead of the original ones, so: "People" for "Persones," "Talent" for "Talent," and "Success" for "Èxit."

The color of the logo can be changed to red, and the overall design can incorporate this color. As the design is for a roll-up, its essential to take into account a 4cm margin.

```html
<!DOCTYPE html>
<html lang="ca">
<head>
<meta charset="utf-8">
<title>Belorqui – Roll-up Nadal 2023</title>
<link rel="stylesheet" href="https://fonts.googleapis.com/css2?family=Bebas+Neue&family=Cinzel:wght@500&family=Montserrat:wght@500;700&family=Libre+Baskerville:wght@400;700&display=swap">
<style>
  :root{
    --page:#eceef1;
    --white:#ffffff;
    --crimson:#b81e4a;
    --crimson-dark:#8f1537;
    --navy:#0c1a4d;
    --sky-top:#1e4d9a;
    --night:#050608;
    --gold:#f5c400;
    --ink:#1f1f24;
  }
  *{margin:0;padding:0;box-sizing:border-box}
  html,body{width:1200px;height:1117px;overflow:hidden;background:var(--page)}
  .canvas{position:relative;width:1200px;height:1117px}
  .rollup{
    position:absolute;left:380px;top:18px;
    width:634px;height:1560px;
    transform:scale(0.6923);transform-origin:top left;
    background:var(--white);overflow:hidden;
    box-shadow:0 6px 24px rgba(0,0,0,.12);
  }
  .rollup-art{position:absolute;inset:0;width:634px;height:1560px}
  .brand{position:absolute;left:0;right:0;top:60px;text-align:center}
  .brand-mark{width:44px;height:44px;border-radius:50%;background:var(--crimson);margin:0 auto 70px}
  .brand-name{font-family:"Cinzel",serif;font-weight:500;font-size:54px;letter-spacing:4px;color:var(--ink);line-height:1}
  .brand-tagline{font-family:"Montserrat",sans-serif;font-weight:500;font-size:17px;letter-spacing:5px;color:var(--crimson);margin-top:10px}
  .headline{position:absolute;left:40px;top:588px;width:560px;font-family:"Bebas Neue",sans-serif;font-weight:400;color:var(--white);line-height:1;white-space:nowrap;text-transform:uppercase}
  .headline .big{font-size:98px;letter-spacing:-1px}
  .headline .small{font-size:74px;letter-spacing:0}
  .edition{position:absolute;left:100px;top:668px;display:flex;align-items:baseline;font-family:"Libre Baskerville",serif;white-space:nowrap;line-height:1}
  .edition-label{font-size:48px;color:var(--white);margin-right:12px}
  .edition-year{font-size:132px;font-weight:700;color:var(--gold);letter-spacing:-4px;line-height:1}
  .values{position:absolute;left:0;top:0}
  .value-label{position:absolute;left:218px;font-family:"Montserrat",sans-serif;font-weight:700;font-size:42px;line-height:1;color:var(--white);text-shadow:2px 3px 4px rgba(0,0,0,.35)}
  .site{position:absolute;left:0;right:0;top:1470px;text-align:center;font-family:"Libre Baskerville",serif;font-weight:700;font-size:36px;color:var(--ink)}
</style>
</head>
<body>
<div class="canvas">
  <div class="rollup">
    <svg class="rollup-art" viewBox="0 0 634 1560" xmlns="http://www.w3.org/2000/svg">
      <defs>
        <linearGradient id="nightSky" x1="0" y1="0" x2="0" y2="1">
          <stop offset="0" stop-color="var(--sky-top)"/>
          <stop offset="0.35" stop-color="#0f2a5c"/>
          <stop offset="0.55" stop-color="var(--night)"/>
          <stop offset="1" stop-color="var(--night)"/>
        </linearGradient>
        <linearGradient id="houses" x1="0" y1="0" x2="1" y2="1">
          <stop offset="0" stop-color="#d9764a"/>
          <stop offset="1" stop-color="#e3aaa0"/>
        </linearGradient>
        <linearGradient id="panel" x1="0" y1="0" x2="1" y2="0">
          <stop offset="0" stop-color="#d52a5a"/>
          <stop offset="1" stop-color="var(--crimson)"/>
        </linearGradient>
      </defs>

      <path role="img" aria-label="Night city skyline under falling snow"
            fill="url(#nightSky)"
            d="M0,262 L360,360 Q410,374 450,340 L634,155 L634,1400 L0,1400 Z"/>
      <rect role="img" aria-label="Snow-covered houses with festive lights"
            x="340" y="860" width="294" height="540" fill="url(#houses)"/>
      <rect x="340" y="1330" width="294" height="70" fill="#5c5c60"/>
      <path d="M0,1390 L634,1390 L634,1560 L0,1560 Z" fill="var(--white)"/>

      <path d="M0,745 L440,880 Q495,897 472,950 L330,1392 Q315,1432 268,1432 L0,1432 Z"
            fill="url(#panel)" stroke="var(--crimson-dark)" stroke-width="8"/>

      <g class="value-divider" stroke="var(--crimson-dark)" stroke-width="4">
        <line x1="220" y1="1030" x2="395" y2="1030"/>
        <line x1="220" y1="1200" x2="345" y2="1200"/>
      </g>

      <g class="value-badge" transform="translate(123,945)">
        <circle r="72" fill="var(--white)"/><circle r="64" fill="var(--navy)"/>
        <g fill="var(--white)">
          <circle cx="-22" cy="-18" r="10"/><circle cx="22" cy="-18" r="10"/><circle cx="0" cy="-10" r="12"/>
          <path d="M-40,14 Q-40,-4 -22,-4 Q-4,-4 -4,14 Z"/><path d="M4,14 Q4,-4 22,-4 Q40,-4 40,14 Z"/>
          <path d="M-22,28 Q-22,4 0,4 Q22,4 22,28 Z"/>
        </g>
      </g>
      <g class="value-badge" transform="translate(123,1115)">
        <circle r="72" fill="var(--white)"/><circle r="64" fill="var(--navy)"/>
        <g fill="var(--white)">
          <path d="M0,-40 L5,-28 L18,-28 L8,-20 L12,-7 L0,-15 L-12,-7 L-8,-20 L-18,-28 L-5,-28 Z"/>
          <circle cx="0" cy="6" r="11"/><path d="M-22,38 Q-22,18 0,18 Q22,18 22,38 Z"/>
        </g>
        <g stroke="var(--white)" stroke-width="3" stroke-linecap="round">
          <line x1="-36" y1="-14" x2="-26" y2="-8"/><line x1="36" y1="-14" x2="26" y2="-8"/>
          <line x1="-38" y1="4" x2="-28" y2="4"/><line x1="38" y1="4" x2="28" y2="4"/>
        </g>
      </g>
      <g class="value-badge" transform="translate(123,1285)">
        <circle r="72" fill="var(--white)"/><circle r="64" fill="var(--navy)"/>
        <g fill="var(--white)">
          <path d="M0,-36 L4,-26 L14,-26 L6,-20 L9,-10 L0,-16 L-9,-10 L-6,-20 L-14,-26 L-4,-26 Z"/>
          <circle cx="0" cy="2" r="10"/>
          <path d="M-26,-8 L-18,-8 L-18,10 Q-18,18 0,18 Q18,18 18,10 L18,-8 L26,-8 L26,14 Q26,26 12,28 L12,38 L-12,38 L-12,28 Q-26,26 -26,14 Z"/>
        </g>
        <g stroke="var(--white)" stroke-width="3" stroke-linecap="round">
          <line x1="-26" y1="-30" x2="-18" y2="-20"/><line x1="26" y1="-30" x2="18" y2="-20"/>
        </g>
      </g>

      <rect x="0" y="1525" width="634" height="35" fill="var(--navy)"/>
    </svg>

    <header class="brand">
      <div class="brand-mark"></div>
      <div class="brand-name">BELORQUI</div>
      <div class="brand-tagline">SELECCIÓ DE TALENT</div>
    </header>

    <h1 class="headline"><span class="big">Seleccio</span> <span class="small">de talent</span></h1>
    <div class="edition"><span class="edition-label">Nadal</span><span class="edition-year">2023</span></div>

    <div class="values">
      <span class="value-label" style="top:922px">People</span>
      <span class="value-label" style="top:1092px">Talent</span>
      <span class="value-label" style="top:1262px">Success</span>
    </div>

    <div class="site">www.BELORQUIS.com</div>
  </div>
</div>
</body>
</html>
```